Hot sauce company needs a logo and label design- simple, clean & fresh

Toby K's a hot pepper sauce company based on the edge of London needs a logo and label design .
The sauces are handmade in small batches with natural ingredients , no added sugars or extracts and so we would like a clean fresh label to reflect this - avoiding all the macho devil and flames novelty stuff.
At present there are four sauces - Jalapeno ,Chipotle,Habanero and Reaper we would like to have one Toby K's label with the name of the sauce being changeable allowing us to react to what ingredients are available .
Updates

Project Deadline Extended
Reason: Hi Guys I have received a few requests to extend the deadline on the project and so I am thanks Toby K's

Target Market(s)

people who care what they eat

Industry/Entity Type

Food Store

Logo Text

Toby K's handmade hot sauce

Requirements
Must have
• Toby K's handmade hot sauce - or the logo
• the name of the sauce Green Serrano
• no added sugars
Nice to have
• handmade
• small batch
Should not have
• cartoon men with smoke coming out of their ears
• devils and the flames of hell

```html
<!DOCTYPE html>
<html lang="en">
<head>
<meta charset="utf-8">
<title>Toby K's Handmade Hot Sauce – Label</title>
<link rel="stylesheet" href="https://fonts.googleapis.com/css2?family=Oswald:wght@600;700&family=Cinzel:wght@600;700&display=swap">
<style>
  :root {
    --cream: #fff9da;
    --outline: #333333;
    --tan: #d2a96b;
    --gold: #f2c23a;
    --blue-deep: #1d4a8f;
    --blue-mid: #1a78c4;
    --blue-light: #1fa6e6;
    --brand-yellow: #ffd21f;
    --white: #ffffff;
    --green-dark: #1f7a33;
    --green-light: #4cae3e;
    --charcoal: #333333;
    --flourish: #9fd6f3;
  }
  html, body {
    margin: 0;
    padding: 0;
    width: 1200px;
    height: 1032px;
    overflow: hidden;
    background: #ffffff;
  }
  .label {
    display: block;
    width: 1200px;
    height: 1032px;
  }
  .label__brand {
    font-family: "Oswald", sans-serif;
    font-weight: 700;
    fill: var(--brand-yellow);
  }
  .label__tagline {
    font-family: "Oswald", sans-serif;
    font-weight: 600;
    fill: var(--white);
  }
  .label__variety {
    font-family: "Cinzel", serif;
    font-weight: 700;
    fill: url(#variety-green);
  }
  .label__claim {
    font-family: "Cinzel", serif;
    font-weight: 600;
    fill: var(--charcoal);
  }
</style>
</head>
<body>
<svg class="label" viewBox="0 0 1200 1032" xmlns="http://www.w3.org/2000/svg" aria-labelledby="label-title">
  <title id="label-title">Toby K's Handmade Hot Sauce – Green Serrano, no added sugars</title>
  <defs>
    <radialGradient id="badge-blue" cx="50%" cy="55%" r="60%">
      <stop offset="0%" stop-color="var(--blue-light)"/>
      <stop offset="55%" stop-color="var(--blue-mid)"/>
      <stop offset="100%" stop-color="var(--blue-deep)"/>
    </radialGradient>
    <linearGradient id="variety-green" x1="0" y1="0" x2="0" y2="1">
      <stop offset="0%" stop-color="var(--green-light)"/>
      <stop offset="100%" stop-color="var(--green-dark)"/>
    </linearGradient>
    <linearGradient id="chilli-tones" x1="0" y1="0" x2="0" y2="1">
      <stop offset="0%" stop-color="#2f9e3f"/>
      <stop offset="45%" stop-color="#e23a2e"/>
      <stop offset="100%" stop-color="#c92a22"/>
    </linearGradient>
    <path id="badge-shape" d="M600,45 Q640,45 660,75 L900,75 Q1000,75 1030,180 Q1080,195 1090,290 Q1150,330 1165,378 Q1150,420 1100,450 Q1090,580 1000,615 Q940,690 660,695 Q630,722 600,725 Q570,722 540,695 Q260,690 200,615 Q110,580 100,450 Q50,420 35,378 Q50,330 110,290 Q120,195 170,180 Q200,75 300,75 L540,75 Q560,45 600,45 Z"/>
  </defs>

  <path class="label__body" d="M6,1026 L6,375 Q20,362 40,340 Q62,262 95,228 Q130,205 150,192 Q178,92 300,52 Q360,32 540,35 Q575,6 600,6 Q625,6 660,35 Q840,32 900,52 Q1022,92 1050,192 Q1070,205 1105,228 Q1138,262 1160,340 Q1180,362 1194,375 L1194,1026 Z"
        fill="var(--cream)" stroke="var(--outline)" stroke-width="7" stroke-linejoin="round"/>

  <g class="badge">
    <use href="#badge-shape" fill="var(--tan)"/>
    <use href="#badge-shape" fill="var(--blue-deep)" transform="translate(600 385) scale(0.975 0.955) translate(-600 -385)"/>
    <use href="#badge-shape" fill="none" stroke="var(--gold)" stroke-width="3" transform="translate(600 385) scale(0.955 0.925) translate(-600 -385)"/>
    <use href="#badge-shape" fill="url(#badge-blue)" transform="translate(600 385) scale(0.945 0.91) translate(-600 -385)"/>
  </g>

  <rect class="badge__illustration" role="img" aria-label="Two crossed red chilli peppers with green stems"
        x="505" y="92" width="195" height="198" rx="50" fill="url(#chilli-tones)" opacity="0.9"/>

  <text class="label__brand" x="600" y="440" text-anchor="middle" font-size="157" textLength="880" lengthAdjust="spacingAndGlyphs">TOBY K'S</text>

  <text class="label__tagline" x="600" y="560" text-anchor="middle" font-size="84" textLength="750" lengthAdjust="spacingAndGlyphs">HANDMADE HOT SAUCE</text>

  <rect class="badge__flourish" role="img" aria-label="Light blue decorative scroll flourish"
        x="415" y="592" width="370" height="66" rx="30" fill="var(--flourish)" opacity="0.55"/>

  <text class="label__variety" x="602" y="885" text-anchor="middle" font-size="136" textLength="955" lengthAdjust="spacingAndGlyphs">GREEN SERRANO</text>

  <text class="label__claim" x="588" y="1000" text-anchor="middle" font-size="78" textLength="720" lengthAdjust="spacingAndGlyphs">NO ADDED SUGARS</text>
</svg>
</body>
</html>
```